Business cards for property management company

Need new business cards designed for our property management company and rental community, Amber Knoll Commons. These cards will be primarily picked up by rental applicants.

May be single or double sided design.

I need cards for two different people, listed below. The design can be the same for both, and the only information that will be different is name and email address.

Industry/Entity Type

Property Management

Requirements
Must have
• US standard business card - 2''x3.5'' horizontal design.

1. Logo (attached). The text does not have to stay below the logo, but the card does need to say "Amber Knoll Commons" somewhere on it (does not have to be same font as logo, but those fonts are Americana Extra Bold and BlackJack if needed).
2. Name: one with "Lena Halvorsen" and one with "Dorian Halvorsen"
3. Email address: one with "lena@amberknollhub.com" and one with "dorian@amberknollhub.com"
4. Web address: amberknollhub.com
5. Phone: 281.555.0182
6. Address: 7390 Whitlock Avenue, Dickinson, Texas 77512 (zip code may me omitted, at your discretion)
Should not have
• No rounded corners or special cuts.

No bevel, emboss or shadow effects.

As a note, please do not use our website as a basis for color or design schemes. We are working on a redesign, based around the new logo (attached to brief).

```html
<!DOCTYPE html>
<html lang="en">
<head>
<meta charset="utf-8">
<title>Amber Knoll Commons – Business Card</title>
<link rel="stylesheet" href="https://fonts.googleapis.com/css2?family=Archivo+Black&family=Archivo:wght@800&family=Questrial&display=swap">
<style>
  :root {
    --pattern-yellow: #f4f42a;
    --pattern-mint: #6cc8a6;
    --frame-blue: #0b78a2;
    --panel-white: #ffffff;
    --brand-green: #159a48;
    --ink: #111111;
    --label-blue: #1d6ea6;
    --teal-top: #2cc3c6;
    --teal-bottom: #0a9bb8;
    --accent-yellow: #fbfb3a;
    --text-white: #ffffff;
  }
  * { margin: 0; padding: 0; box-sizing: border-box; }
  html, body { width: 1200px; height: 686px; overflow: hidden; background: #ffffff; }
  .card { position: relative; width: 1200px; height: 686px; overflow: hidden; }
  .card__pattern {
    position: absolute; inset: 0;
    background: linear-gradient(135deg, var(--pattern-yellow), #c9ea6a 55%, var(--pattern-mint));
  }
  .card__frame {
    position: absolute; left: 25px; top: 25px; width: 1150px; height: 640px;
    background: var(--frame-blue);
  }
  .card__panel { position: absolute; left: 0; top: 0; }
  .card__contact-band {
    position: absolute; left: 34px; top: 448px; width: 1132px; height: 213px;
    background: linear-gradient(180deg, var(--teal-top), var(--teal-bottom));
  }
  .brand {
    position: absolute; left: 0; right: 0; top: 82px;
    display: flex; justify-content: center; align-items: center; gap: 22px;
  }
  .brand__dot { width: 58px; height: 58px; border-radius: 50%; background: var(--brand-green); }
  .brand__name {
    font-family: "Archivo Black", sans-serif; font-size: 52px; color: var(--brand-green);
    letter-spacing: 0.5px;
  }
  .names {
    position: absolute; left: 0; right: 0; top: 252px; text-align: center;
    font-family: "Archivo Black", sans-serif; font-size: 36px; color: var(--ink);
  }
  .emails {
    position: absolute; left: 0; right: 0; top: 374px; text-align: center;
    font-family: "Questrial", sans-serif; font-size: 29px; color: var(--ink);
  }
  .emails__label {
    font-family: "Archivo", sans-serif; font-weight: 800; font-size: 22px; color: var(--label-blue);
  }
  .phone, .web {
    position: absolute; left: 0; right: 0; text-align: center;
    font-family: "Archivo", sans-serif; font-weight: 800; font-size: 36px; color: var(--accent-yellow);
    letter-spacing: 1px;
  }
  .phone { top: 494px; }
  .phone__label { font-size: 31px; }
  .address {
    position: absolute; left: 0; right: 0; top: 549px; text-align: center;
    font-family: "Questrial", sans-serif; font-size: 35px; color: var(--text-white); letter-spacing: 0.5px;
  }
  .web { top: 597px; }
</style>
</head>
<body>
  <div class="card">
    <div class="card__pattern" role="img" aria-label="Decorative background of mint green dots on yellow"></div>
    <div class="card__frame"></div>
    <svg class="card__panel" width="1200" height="686" viewBox="0 0 1200 686" aria-hidden="true">
      <polygon points="149,32 1051,32 1166,160 1166,417 34,417 34,150" fill="var(--panel-white)"/>
      <rect x="34" y="437" width="1132" height="11" fill="var(--panel-white)"/>
    </svg>
    <div class="card__contact-band"></div>

    <div class="brand">
      <span class="brand__dot"></span>
      <span class="brand__name">Amber Knoll Commons</span>
    </div>

    <p class="names">Lena Halvorsen &amp; Dorian Halvorsen</p>

    <p class="emails"><span class="emails__label">Email:</span> lena@amberknollhub.com&nbsp; / dorian@amberknollhub.com</p>

    <p class="phone"><span class="phone__label">Phone:</span> 281.555.0182</p>
    <p class="address">7390 Whitlock Avenue, Dickinson, Texas 77512</p>
    <p class="web">amberknollhub.com</p>
  </div>
</body>
</html>
```